Maren Tolliver Luxury Wellness Profile Booklet

I am a luxury wellness property agent and would like to create my personal profile booklet. I want this to feel luxurious, minimalist, informative and the philosophy behind wellness and property the cPAGE 1 — THE COVER

Very minimal.

MAREN TOLLIVER

LUXURY WELLNESS PROPERTY

PROPERTY • WELLNESS • LIFESTYLE

Keel Ashby Coastline Group

Large photograph of you — preferably walking through a beautiful waterfront property or standing naturally within an architectural setting.

At the bottom:

Hope Island • Sanctuary Cove • Helensvale

Small Keel Ashby logo.

PAGE 2 — THE OPENING STATEMENT

A beautiful full-page lifestyle photograph.

Overlaid:

WHERE PROPERTY
MEETS WELLBEING

“A home is more than an address. It is the environment in which life unfolds.”

Then a short introduction:

Opening Profile

I believe the most exceptional properties are not defined simply by their architecture, address or price.

They are defined by how they make you feel.

Natural light. Water views. Privacy. Green space. Indoor-outdoor living. A place to unwind, entertain, recharge and reconnect.

My approach to luxury property brings these elements together — combining strategic real estate expertise with a genuine understanding of wellness, lifestyle and the way people want to live today.

Because when we understand the lifestyle behind the property, we can create a more compelling story around it.

PAGE 3 — MEET MAREN

Large portrait of you on one side.

Other side:

MEET MAREN

20+ YEARS OF PROPERTY EXPERIENCE

Commercial
Residential
Project Sales
Luxury & Lifestyle Property

Then:

About Maren

With more than 20 years' experience across commercial, residential and project sales, I have built my career around relationships, strategic marketing and delivering exceptional outcomes for my clients.

My approach is warm, considered and highly personal.

I believe sellers deserve more than a listing campaign. They deserve a clear strategy, honest communication and an agent who understands what makes their property valuable — both financially and emotionally.

Today, my focus is luxury lifestyle property across the Northern Gold Coast, with a particular passion for Hope Island, Sanctuary Cove and selected waterfront gated estates in Helensvale.

PAGE 4 — WHY WELLNESS?

This is where your differentiation becomes really powerful.

Full-bleed photograph of:

pool
outdoor entertaining
greenery
water
spa
wellness room
person walking beside water
WELLNESS IS THE NEW LUXURY

Then:

Wellness Philosophy

Luxury has evolved.

Today, luxury is not only about beautiful finishes, expansive living spaces or an impressive address.

It is privacy.

It is waking to water.

It is natural light flooding through the home.

It is having space to breathe.

It is stepping outside into nature, walking along the water, enjoying a morning swim, entertaining beside the pool or creating a private sanctuary at home.

These lifestyle elements increasingly shape the way buyers experience and value a property.

This is where my passion for wellness becomes part of my property approach.

PAGE 5 — MY WELLNESS JOURNEY

This page makes the wellness positioning credible rather than simply being a marketing slogan.

MY WELLNESS JOURNEY

You could use 3 small photographs:

BLOOMFOLD TOTS
QUILLON WELLNESS CENTRE
LUXURY WELLNESS PROPERTY

Copy:

Wellness Journey

My connection with wellness began outside of real estate.

After stepping away from property, I founded Bloomfold Tots, developing an organic children's nutritional product with a focus on natural ingredients and wellbeing.

I later launched Quillon Wellness Centre, further deepening my understanding of wellness, health-conscious lifestyles and the importance of creating environments that support how we live.

Today, I bring that perspective back into property.

I see homes differently — not simply as buildings, but as environments for living, restoring, entertaining and thriving.

PAGE 6 — THE MAREN TOLLIVER DIFFERENCE

This should be one of your strongest pages.

A DIFFERENT WAY OF SEEING PROPERTY

Use six elegant icons or small images:

01 — LIFESTYLE

I look beyond the floor plan to understand how buyers will actually experience the home.

02 — WELLNESS

I identify the spaces and features that contribute to wellbeing and lifestyle.

03 — PRESENTATION

I create a campaign that makes the property feel aspirational, memorable and emotionally engaging.

04 — STORY

Every exceptional property has a story. I find it, refine it and communicate it.

05 — STRATEGY

From positioning and buyer targeting to campaign execution and negotiation, every element has a purpose.

06 — RELATIONSHIPS

Trust, transparency and communication remain at the centre of every campaign.

PAGE 7 — YOUR PROPERTY STORY

This could be a beautiful editorial spread.

EVERY HOME HAS A STORY

Then:

My role is to discover what makes yours extraordinary.

Three questions:

WHAT MAKES YOUR PROPERTY DIFFERENT?

Architecture?
Waterfront?
Views?
Privacy?
Garden?
Location?

HOW DOES IT MAKE PEOPLE FEEL?

Calm?
Inspired?
Connected?
Entertained?
Relaxed?

WHO WILL FALL IN LOVE WITH IT?

Families?
Executives?
Downsizers?
Boaties?
Golfers?
Wellness-focused buyers?
Lifestyle purchasers?

Then:

I turn these answers into your property's story.

PAGE 8 — YOUR NORTHERN GOLD COAST

Beautiful aerial/waterfront image.

MY MARKET

HOPE ISLAND

SANCTUARY COVE

HELENSVALE

WATERFRONT & GATED ESTATES

Copy:

Northern Gold Coast

I specialise in the lifestyle-driven property market of the Northern Gold Coast.

From the waterfront homes and private enclaves of Hope Island and Sanctuary Cove to the established gated estates of Helensvale, I understand the lifestyle characteristics that attract buyers to this part of the Gold Coast.

Having personally experienced the lifestyle of these communities, I understand that buyers are often purchasing far more than a house.

They are buying a way of life.

PAGE 9 — THE WELLNESS PROPERTY

This could become your signature page.

WHAT MAKES A WELLNESS HOME?

Use a sophisticated grid:

WATER
Pools • Waterfront • Marina • Water views

NATURE
Green space • Gardens • Reserve outlooks • Walking trails

LIGHT
Natural light • Orientation • Open spaces

MOVEMENT
Walking • Golf • Boating • Outdoor living

RESTORATION
Spa • Sauna • Cold plunge • Retreat spaces

CONNECTION
Entertaining • Family • Indoor/outdoor living

Bottom:

The most desirable luxury is often the way a home makes you feel.

PAGE 10 — THE SELLING EXPERIENCE
YOUR HOME. YOUR STORY. YOUR CAMPAIGN.

I would make this a simple six-stage journey:

01 — DISCOVER
Understand your property, your goals and your lifestyle.

↓

02 — POSITION
Establish the property's unique market position.

↓

03 — PREPARE
Presentation, styling and strategic recommendations.

↓

04 — CREATE
Photography, film, editorial storytelling and digital marketing.

↓

05 — CONNECT
Targeted buyer engagement and database activation.

↓

06 — NEGOTIATE
Strategic negotiation designed to maximise the opportunity.

PAGE 11 — THE POWER OF PRESENTATION

Large before/after style photography.

FIRST IMPRESSIONS ARE EVERYTHING

Copy:

We don't get a second opportunity to create a first impression.

Then explain your approach to:

styling
photography
cinematic video
twilight imagery
aerial photography
lifestyle storytelling
digital advertising
targeted database marketing
buyer follow-up
auction strategy

Importantly, don't make this page feel like a generic list of marketing products.

Frame everything around:

Creating desire before creating urgency.
PAGE 12 — PROVEN RESULTS

Now introduce your actual results.

RESULTS THAT BUILD CONFIDENCE

Use your strongest results as elegant case studies.

For example:
4183 Pellingham Drive, Hope Island
$3,850,000
34 Days On The Market

$2.90M
52 Amberlyn Vale Boulevard, Helensvale
Sold within 45 days

Include your result and the property's story.

$2.15M

3/9 Amberlyn Vale Boulevard

Waterfront Villa

Then potentially:

28 DAYS

5218 Thistlewood Boulevard, Hope Island

Under contract following relaunch

If a result subsequently changed because the contract fell through, be careful about how you describe the current status. We can make this page completely accurate to the final outcome.

PAGE 13 — THE KEEL ASHBY ADVANTAGE

This is where you let the brand support you, rather than letting the booklet become a Keel Ashby corporate brochure.

PERSONAL SERVICE.
NATIONAL REACH.

Then a short statement about your Keel Ashby platform.

You could include:

POWERFUL BUYER DATABASE

LUXURY PROPERTY MARKETING

AUCTION EXPERTISE

DIGITAL REACH

LOCAL KNOWLEDGE

NATIONAL NETWORK

And a short line:

The personal attention of a specialist agent, supported by the strength of a globally recognised property network.

PAGE 14 — WHAT YOU CAN EXPECT FROM ME

This page is very important for your seller proposition.

MY PROMISE TO YOU

TRANSPARENCY

Clear advice, honest feedback and no unnecessary promises.

COMMUNICATION

You will know what is happening throughout your campaign.

STRATEGY

Every decision is made with your property, market and objectives in mind.

ATTENTION TO DETAIL

Your home deserves meticulous preparation and presentation.

PERSONAL SERVICE

You deal directly with me throughout your campaign.

RESULT FOCUS

My role is to create the strongest possible environment for a successful sale.

PAGE 15 — THE CLOSING PAGE

This should be very luxurious and emotional.

Beautiful photograph of water at sunset / luxury pool / Hope Island lifestyle.

YOUR HOME.
YOUR NEXT CHAPTER.

Then:

Closing Statement

Selling a home is rarely just a transaction.

It is the closing of one chapter and the beginning of another.

My role is to make the journey feel considered, strategic and personal — while creating the strongest possible opportunity for your property in the marketplace.

Thank you for considering me to represent your home.

I would be honoured to tell its story.

Then your details:

MAREN TOLLIVER

Luxury Wellness Property

0471 536 802

BACK COVER

Keep it extremely clean.

Your photograph or perhaps a beautiful Gold Coast waterfront image.

MAREN TOLLIVER

LUXURY WELLNESS PROPERTY

0471 536 802

Keel Ashby logoollaboration. I can send a full brief if required.

Target Market(s)

Luxury Property Owners

Industry/Entity Type

Wellness Luxury Real Estate Lifestyle

Requirements
Must have
• A luxurious minimalist clean feel

```html
<!DOCTYPE html>
<html lang="en">
<head>
<meta charset="utf-8">
<title>Maren Tolliver — Luxury Wellness Property</title>
<link rel="stylesheet" href="https://fonts.googleapis.com/css2?family=Cinzel:wght@400;500&family=Montserrat:wght@300;400&family=Cormorant+Garamond:wght@400;500&family=Allura&display=swap">
<style>
  :root {
    --ink: #1e1e1e;
    --ink-soft: #3c3a37;
    --gold: #a8864f;
    --paper: #f7f6f3;
    --sky-top: #eceef0;
    --sky-warm: #f2dcc3;
    --water: #6e95a1;
    --water-deep: #4f7480;
    --terrace: #e8e6e2;
    --cream: #efe8dc;
    --cream-deep: #ddd3c3;
    --white: #ffffff;
  }
  * { margin: 0; padding: 0; box-sizing: border-box; }
  html, body { width: 1147px; height: 1200px; overflow: hidden; background: var(--paper); }
  .cover {
    position: relative;
    width: 1147px;
    height: 1200px;
    overflow: hidden;
    background: var(--paper);
    font-family: "Montserrat", sans-serif;
    color: var(--ink);
  }
  .cover-photo {
    position: absolute;
    inset: 0 0 110px 0;
    background:
      linear-gradient(180deg,
        var(--sky-top) 0%,
        #efe7dd 30%,
        var(--sky-warm) 44%,
        #b9b9a6 52%,
        var(--water) 62%,
        var(--water-deep) 74%,
        #a9bcc0 84%,
        var(--terrace) 100%);
  }
  .cover-photo::after {
    content: "";
    position: absolute;
    inset: 0;
    background: linear-gradient(180deg, rgba(255,255,255,0.55) 0%, rgba(255,255,255,0) 32%);
  }
  .portrait {
    position: absolute;
    top: 380px;
    left: 435px;
    width: 290px;
    height: 710px;
    border-radius: 120px 120px 0 0;
    background: linear-gradient(180deg, #e6d3b4 0%, var(--cream) 22%, #f1ece3 60%, var(--cream-deep) 85%, rgba(232,230,226,0.6) 100%);
  }
  .masthead {
    position: absolute;
    top: 130px;
    left: 0;
    width: 100%;
    text-align: center;
  }
  .agent-name {
    font-family: "Cinzel", serif;
    font-weight: 400;
    font-size: 88px;
    letter-spacing: 4px;
    line-height: 1;
    color: var(--ink);
  }
  .agent-title {
    margin-top: 22px;
    font-weight: 300;
    font-size: 28px;
    letter-spacing: 9px;
    color: var(--ink-soft);
  }
  .rule {
    display: block;
    height: 2px;
    background: var(--gold);
  }
  .masthead .rule { width: 84px; margin: 22px auto 0; }
  .pillars {
    margin-top: 30px;
    font-weight: 400;
    font-size: 17px;
    letter-spacing: 5px;
    color: var(--ink-soft);
  }
  .pillars .dot { margin: 0 14px; }
  .ethos {
    position: absolute;
    top: 400px;
    left: 110px;
    font-family: "Cormorant Garamond", serif;
    font-weight: 500;
    font-size: 21px;
    line-height: 1.2;
    letter-spacing: 3px;
    color: #5a4e40;
  }
  .ethos .rule { width: 60px; margin-top: 26px; }
  .motto {
    position: absolute;
    top: 640px;
    left: 770px;
    width: 300px;
    font-family: "Allura", cursive;
    font-size: 52px;
    line-height: 1.05;
    color: var(--white);
  }
  .motto .rule { width: 60px; margin: 20px 0 0 70px; }
  .brand {
    position: absolute;
    top: 905px;
    right: 40px;
    width: 200px;
    display: flex;
    flex-direction: column;
    align-items: center;
    gap: 12px;
    font-family: "Montserrat", sans-serif;
    font-weight: 400;
    font-size: 13px;
    color: var(--ink);
  }
  .brand-square { width: 120px; height: 120px; background: var(--gold); }
  .locations {
    position: absolute;
    bottom: 0;
    left: 0;
    width: 100%;
    height: 150px;
    padding-top: 64px;
    text-align: center;
    font-weight: 400;
    font-size: 19px;
    letter-spacing: 6px;
    color: var(--ink-soft);
    background: linear-gradient(180deg, rgba(247,246,243,0) 0%, var(--paper) 40%);
  }
  .locations .dot { margin: 0 14px; }
</style>
</head>
<body>
  <main class="cover">
    <div class="cover-photo" role="img" aria-label="Waterfront pool terrace at sunset with palm trees, marina boats and villas"></div>
    <div class="portrait" role="img" aria-label="Portrait of the agent in a cream suit walking along the terrace"></div>

    <header class="masthead">
      <h1 class="agent-name">MAREN TOLLIVER</h1>
      <p class="agent-title">LUXURY WELLNESS PROPERTY</p>
      <span class="rule"></span>
      <p class="pillars">PROPERTY<span class="dot">•</span>WELLNESS<span class="dot">•</span>LIFESTYLE</p>
    </header>

    <div class="ethos">
      <p>EXCEPTIONAL<br>PROPERTIES<br>HEALTHIER<br>PEOPLE<br>HAPPIER<br>COMMUNITIES</p>
      <span class="rule"></span>
    </div>

    <div class="motto">
      <p>More Than<br>Property<br>A Better<br>Way to Live</p>
      <span class="rule"></span>
    </div>

    <div class="brand">
      <span class="brand-square"></span>
      <span class="brand-name">Keel Ashby Coastline Group</span>
    </div>

    <footer class="locations">HOPE ISLAND<span class="dot">•</span>SANCTUARY COVE<span class="dot">•</span>HELENSVALE</footer>
  </main>
</body>
</html>
```